Professional DJ Business Card

Business card for giving out to clubs and venues or interested groups that are in need of a professional DJ. I want something artistic and catchy/alluring, with a minimalist approach that gets just the vital amount of info and leaves the rest for inquiry via contacting me. Ideally I would like one side to have an image of something cool like an eye and my name, then the other side be the contact info, I am definitely feeling a black or dark colored card, but I am open to other designs. I am uploading a picture that I made that reflects a little of what I am *kind of* looking for.

Industry/Entity Type

Business

Contact Information for Business Card

Tomas Velander (Kalvo)
Professional DJ (West Coast)
EDM (Deep/House/Techno), Hip Hop, Latin, Trap.
Cell: 555-274-8391
Email: Kalvoofficial@mailbrook.net
www.tunevault.net/oxfernwaits

```html
<!DOCTYPE html>
<html lang="en">
<head>
<meta charset="utf-8">
<title>Kalvo – DJ Business Card</title>
<link rel="stylesheet" href="https://fonts.googleapis.com/css2?family=Jost:wght@400;700;800&display=swap">
<style>
  :root {
    --page: #ffffff;
    --card: #000000;
    --ink: #ffffff;
    --band: #ffffff;
    --band-ink: #000000;
  }
  * { margin: 0; padding: 0; box-sizing: border-box; }
  html, body {
    width: 1200px;
    height: 849px;
    overflow: hidden;
    background: var(--page);
  }
  .sheet {
    position: relative;
    width: 1200px;
    height: 849px;
    font-family: "Jost", "Futura", sans-serif;
    color: var(--ink);
  }
  .card {
    position: absolute;
    left: 305px;
    width: 578px;
    height: 321px;
    background: var(--card);
  }
  .card--front { top: 76px; }
  .card--back { top: 443px; }

  .wordmark {
    position: absolute;
    left: 0;
    right: 0;
    top: 190px;
    transform: translateY(-50%);
    text-align: center;
    font-weight: 700;
    font-size: 80px;
    letter-spacing: 4px;
    line-height: 1;
    color: var(--ink);
  }

  .contact {
    position: absolute;
    left: 0;
    right: 0;
    top: 72px;
    text-align: center;
  }
  .contact__name {
    font-weight: 800;
    font-size: 22px;
    line-height: 28px;
    letter-spacing: 0.3px;
  }
  .contact__role {
    font-weight: 400;
    font-size: 17px;
    line-height: 22px;
    margin-bottom: 26px;
  }
  .contact__line {
    font-weight: 400;
    font-size: 17px;
    line-height: 26px;
  }

  .genres {
    position: absolute;
    left: 0;
    right: 0;
    top: 269px;
    height: 31px;
    background: var(--band);
    color: var(--band-ink);
    text-align: center;
    font-weight: 400;
    font-size: 18px;
    line-height: 31px;
    letter-spacing: 0.3px;
  }
</style>
</head>
<body>
  <main class="sheet">
    <section class="card card--front">
      <h1 class="wordmark">KALVO</h1>
    </section>

    <section class="card card--back">
      <div class="contact">
        <p class="contact__name">Tomas Velander (Kalvo)</p>
        <p class="contact__role">Professional DJ (West Coast)</p>
        <p class="contact__line">Cell: 555-274-8391</p>
        <p class="contact__line">Email: Kalvoofficial@mailbrook.net</p>
        <p class="contact__line">www.tunevault.net/oxfernwaits</p>
      </div>
      <p class="genres">• EDM (Deep/House/Techno) • Hip Hop • Latin • Trap.</p>
    </section>
  </main>
</body>
</html>
```